Business Card & Letterhead Design

We a financial advice company based in Australia. We provide advice to wealthy farmers.

We are changing our business name FROM Brightmere Financial TO Calderstone Wealth and we need a new letterhead and double sided business card design

Attached is designs from our previous branding (Brightmere Financial) as it includes all the details we require on the new Calderstone Wealth business cards and letterhead.

```html
<!DOCTYPE html>
<html lang="en">
<head>
<meta charset="utf-8">
<title>Calderstone Wealth Stationery</title>
<link rel="stylesheet" href="https://fonts.googleapis.com/css2?family=Cinzel:wght@400&family=Montserrat:wght@400&family=Open+Sans:wght@400;600&family=Arimo&display=swap">
<style>
:root{
  --board:#c8c8c8;
  --ink:#524e4d;
  --stripe:#6b7278;
  --paper:#ffffff;
  --faint:#f1f1f1;
  --window:#ececec;
  --tag:#8a8685;
}
*{margin:0;padding:0;box-sizing:border-box}
html,body{width:1200px;height:958px;overflow:hidden;background:var(--board)}
.board{position:relative;width:1200px;height:958px}
.piece{position:absolute;overflow:hidden;background:var(--paper)}
.piece.dark{background:var(--ink)}
.brand{position:absolute;left:0;right:0;text-align:center}
.brand-ring{display:block;margin:0 auto;border:1.5px solid var(--ink);border-radius:50%}
.dark .brand-ring{border-color:var(--paper)}
.brand-name{font-family:"Cinzel",serif;font-weight:400;color:var(--ink);white-space:nowrap;line-height:1}
.dark .brand-name{color:var(--paper)}
.brand-tag{font-family:"Montserrat",sans-serif;color:var(--tag);letter-spacing:.32em;text-transform:uppercase;white-space:nowrap;line-height:1}
.dark .brand-tag{color:#9b9796}
.motto{position:absolute;font-family:"Open Sans",sans-serif;text-transform:uppercase;white-space:nowrap}

/* cards */
.card{top:38px;width:211px;height:121px}
.card .brand{top:30px}
.card .brand-ring{width:38px;height:38px}
.card .brand-name{font-size:12px;margin-top:11px}
.card .brand-tag{font-size:4.6px;margin-top:2px}
.card .motto{left:0;right:0;top:105px;text-align:center;font-size:5.4px;color:var(--paper)}
.card.light .motto{color:var(--ink)}
.card.one{left:47px}.card.two{left:341px}.card.three{left:634px}.card.four{left:928px}
.watermark-ring{position:absolute;border-radius:50%;border:6px solid rgba(255,255,255,.05)}

.card.four .brand{top:8px;left:0;width:130px}
.card.four .brand-ring{width:26px;height:26px}
.card.four .brand-name{font-size:10px;margin-top:6px}
.card.four .brand-tag{font-size:3.6px;margin-top:1px}
.card-wave{position:absolute;left:0;top:0}
.contact-person{position:absolute;right:11px;top:46px;text-align:right;font-family:"Open Sans",sans-serif;color:var(--ink)}
.contact-person .who{font-size:6.4px;font-weight:600;line-height:8px}
.contact-person .role{font-size:4.6px;line-height:6.6px}
.card-contact{position:absolute;right:11px;top:84px;text-align:right;font-family:"Open Sans",sans-serif;font-size:4.8px;line-height:7px;color:var(--paper);list-style:none}
.card-contact li{display:flex;justify-content:flex-end;align-items:center;gap:3px;white-space:nowrap}
.card-contact svg{width:4px;height:4px;fill:var(--paper)}
.card-address{position:absolute;left:11px;top:96px;font-family:"Open Sans",sans-serif;font-size:4.8px;line-height:7px;color:var(--paper);white-space:nowrap}
.wave{position:absolute;left:0;width:100%}

/* letterhead */
.letterhead{left:45px;top:196px;width:500px;height:707px;border-top:2.5px solid var(--ink)}
.letterhead .brand{top:26px;left:0;width:244px}
.letterhead .brand-ring{width:45px;height:45px}
.letterhead .brand-name{font-size:15px;margin-top:10px}
.letterhead .brand-tag{font-size:5.6px;margin-top:2px}
.sender{position:absolute;left:352px;top:30px;padding-left:9px;border-left:1px solid var(--ink);font-family:"Open Sans",sans-serif;font-size:7px;line-height:9.3px;color:var(--ink);height:120px}
.sender .firm{font-weight:600;font-size:7.4px}
.sender p{margin-bottom:6px}
.sender li{list-style:none;display:flex;align-items:center;gap:6px}
.sender svg{width:6px;height:6px;fill:var(--ink)}
.big-ring{position:absolute;border-radius:50%;border:4px solid var(--faint)}
.legal{position:absolute;top:632px;left:0;width:100%;font-family:"Arimo",sans-serif;font-size:7.2px;line-height:8.4px;color:var(--ink)}
.legal div{position:absolute;top:0;white-space:nowrap}
.legal .rule{width:1px;height:14px;background:var(--ink);top:2px}
.letterhead .motto{right:30px;top:683px;font-size:7.2px;color:var(--paper)}

/* envelopes */
.envelope{left:616px;width:523px;height:262px}
.envelope.flap{top:293px}
.flap-shape{position:absolute;top:0;left:0}
.envelope.flap .flap-ring{position:absolute;left:242px;top:20px;width:40px;height:40px;border:1.5px solid var(--paper);border-radius:50%}
.envelope.flap .brand-tag{position:absolute;left:0;right:0;top:62px;text-align:center;font-size:4.4px;color:#5e5a59}
.return-line{position:absolute;left:0;right:0;top:235px;text-align:center;font-family:"Open Sans",sans-serif;font-size:6px;color:var(--ink)}
.envelope.window{top:643px;height:262px}
.envelope.window .brand{top:28px;left:0;width:231px}
.envelope.window .brand-ring{width:38px;height:38px}
.envelope.window .brand-name{font-size:13px;margin-top:8px}
.envelope.window .brand-tag{font-size:5px;margin-top:2px}
.address-window{position:absolute;left:35px;top:118px;width:207px;height:90px;border-radius:5px;background:var(--window);border:1px solid #dcdcdc}
.envelope.window .motto{top:240px;right:30px;font-size:7.2px;color:var(--paper)}
</style>
</head>
<body>
<main class="board">

  <section class="piece card dark one">
    <div class="brand"><span class="brand-ring"></span><div class="brand-name">Calderstone Wealth</div><div class="brand-tag">Strategic Financial Advice</div></div>
    <div class="motto">Financial Peace of Mind</div>
  </section>

  <section class="piece card light two">
    <div class="brand"><span class="brand-ring"></span><div class="brand-name">Calderstone Wealth</div><div class="brand-tag">Strategic Financial Advice</div></div>
    <div class="motto">Financial Peace of Mind</div>
  </section>

  <section class="piece card dark three">
    <div class="watermark-ring" style="left:25px;top:-20px;width:160px;height:160px"></div>
    <div class="brand"><span class="brand-ring"></span><div class="brand-name">Calderstone Wealth</div><div class="brand-tag">Strategic Financial Advice</div></div>
    <div class="motto">Financial Peace of Mind</div>
  </section>

  <section class="piece card four">
    <svg class="card-wave" width="211" height="121" viewBox="0 0 211 121">
      <path d="M0,78 C70,82 140,79 211,76 V121 H0Z" fill="#524e4d"/>
      <path d="M0,66 C60,74 115,68 155,48 C178,37 195,33 211,32 L211,34.5 C195,35.5 178,39.5 155,50.5 C115,70.5 60,76.5 0,68.5Z" fill="#524e4d"/>
      <path d="M0,70 C60,78 115,72 155,52 C178,41 195,37 211,36 L211,39 C195,40 178,44 155,55 C115,75 60,81 0,73.5Z" fill="#6b7278"/>
    </svg>
    <div class="brand"><span class="brand-ring"></span><div class="brand-name">Calderstone Wealth</div><div class="brand-tag">Strategic Financial Advice</div></div>
    <div class="contact-person">
      <div class="who">Tom Reyes</div>
      <div class="role">B.Ag.Ec. Dip F.P. CFP<br>Managing Director<br>Authorised Representative</div>
    </div>
    <div class="card-address">Suite 4A, 18 Harlow St<br>Riverton QLD 4170<br>PO Box 5120, Eastvale QLD 4170</div>
    <ul class="card-contact">
      <li>(07) 3100 2040<svg viewBox="0 0 10 10"><path d="M2,0 L4,2 L3,3.5 C4,5.5 4.5,6 6.5,7 L8,6 L10,8 L8,10 C4,9.5 0.5,6 0,2Z"/></svg></li>
      <li>(07) 3100 2041<svg viewBox="0 0 10 10"><rect x="2" y="0" width="6" height="3"/><rect x="0" y="3.5" width="10" height="4"/><rect x="2" y="8" width="6" height="2"/></svg></li>
      <li>0400 555 218<svg viewBox="0 0 10 10"><rect x="2.5" y="0" width="5" height="10" rx="1"/></svg></li>
      <li>info@calderstonewealth.com.au<svg viewBox="0 0 10 10"><rect x="0" y="2" width="10" height="6"/></svg></li>
      <li>www.calderstonewealth.com.au<svg viewBox="0 0 10 10"><circle cx="5" cy="5" r="5"/></svg></li>
    </ul>
  </section>

  <section class="piece letterhead">
    <div class="big-ring" style="left:93px;top:270px;width:314px;height:314px"></div>
    <div class="brand"><span class="brand-ring"></span><div class="brand-name">Calderstone Wealth</div><div class="brand-tag">Strategic Financial Advice</div></div>
    <div class="sender">
      <p><span class="firm">Calderstone Wealth</span><br>Corporate Authorised<br>Representative of Marlow<br>Financial Planning Limited</p>
      <p>Suite 4A, 18 Harlow St<br>Riverton QLD 4170<br>PO Box 5120<br>Eastvale QLD 4170</p>
      <ul>
        <li><svg viewBox="0 0 10 10"><path d="M2,0 L4,2 L3,3.5 C4,5.5 4.5,6 6.5,7 L8,6 L10,8 L8,10 C4,9.5 0.5,6 0,2Z"/></svg>(07) 3100 2040</li>
        <li><svg viewBox="0 0 10 10"><rect x="2" y="0" width="6" height="3"/><rect x="0" y="3.5" width="10" height="4"/><rect x="2" y="8" width="6" height="2"/></svg>(07) 3100 2041</li>
        <li><svg viewBox="0 0 10 10"><rect x="0" y="2" width="10" height="6"/></svg>info@calderstonewealth.com.au</li>
        <li><svg viewBox="0 0 10 10"><circle cx="5" cy="5" r="5"/></svg>www.calderstonewealth.com.au</li>
      </ul>
    </div>
    <div class="legal">
      <div style="left:40px">Marlow Financial Planning Limited<br>ABN 12 345 678 901</div>
      <div class="rule" style="left:172px"></div>
      <div style="left:194px">Australian Financial Services Licence<br>Licence Number 456 789</div>
      <div class="rule" style="left:335px"></div>
      <div style="left:357px">Principal Address: 410 Ferris St<br>PO Box 1180 Southbank VIC 3006</div>
    </div>
    <svg class="wave" style="top:650px" width="500" height="57" viewBox="0 0 500 57" preserveAspectRatio="none">
      <path d="M0,16 C120,24 220,46 330,30 C410,18 460,14 500,12 V57 H0Z" fill="#524e4d"/>
      <path d="M0,9 C120,18 220,40 330,23 C410,10 460,4 500,2 L500,6 C460,8 410,14 330,26 C220,44 120,22 0,13Z" fill="#524e4d"/>
      <path d="M0,19 C120,28 220,50 330,33 C410,21 460,17 500,15 L500,19 C460,20 410,24 330,36 C220,53 120,32 0,24Z" fill="#6b7278"/>
      <path d="M0,13 C120,22 220,44 330,26 C410,14 460,8 500,6 L500,12 C460,14 410,18 330,30 C220,46 120,24 0,16Z" fill="#ffffff"/>
    </svg>
    <div class="motto">Financial Peace of Mind</div>
  </section>

  <section class="piece envelope flap">
    <svg class="flap-shape" width="523" height="78" viewBox="0 0 523 78">
      <path d="M0,0 H523 L504,64 Q500,78 486,78 H37 Q23,78 19,64 Z" fill="#524e4d"/>
    </svg>
    <span class="flap-ring"></span>
    <div class="brand-tag">Strategic Financial Advice</div>
    <div class="return-line">Calderstone Wealth • Suite 4A, 18 Harlow St • Riverton QLD 4170 • PO Box 5120 • Eastvale QLD 4170</div>
  </section>

  <section class="piece envelope window">
    <div class="big-ring" style="left:348px;top:-2px;width:180px;height:180px"></div>
    <div class="brand"><span class="brand-ring"></span><div class="brand-name">Calderstone Wealth</div><div class="brand-tag">Strategic Financial Advice</div></div>
    <div class="address-window"></div>
    <svg class="wave" style="top:205px" width="524" height="57" viewBox="0 0 524 57" preserveAspectRatio="none">
      <path d="M0,16 C120,24 220,42 340,30 C420,20 480,16 524,14 V57 H0Z" fill="#524e4d"/>
      <path d="M0,9 C120,18 220,36 340,23 C420,12 480,6 524,4 L524,8 C480,10 420,16 340,26 C220,40 120,22 0,13Z" fill="#524e4d"/>
      <path d="M0,19 C120,28 220,46 340,33 C420,23 480,19 524,17 L524,21 C480,22 420,26 340,36 C220,49 120,32 0,24Z" fill="#6b7278"/>
      <path d="M0,13 C120,22 220,40 340,26 C420,16 480,10 524,8 L524,14 C480,16 420,20 340,30 C220,42 120,24 0,16Z" fill="#ffffff"/>
    </svg>
    <div class="motto">Financial Peace of Mind</div>
  </section>

</main>
</body>
</html>
```